Business Card - Cooperate

Business Card for Larkfield Management Consulting

Target Market(s)

Corparte - b2B

Industry/Entity Type

Management Consulting - Professional Services

Contact Information for Business Card

Company Name , Slogan , Dummy Address,

Requirements
Must have
• Reach your Full Potential

```html
<!DOCTYPE html>
<html lang="en">
<head>
<meta charset="utf-8">
<title>Larkfield Management Consulting – Business Card</title>
<link rel="stylesheet" href="https://fonts.googleapis.com/css2?family=Poppins:wght@400;500;600;700&display=swap">
<style>
  :root {
    --canvas: #2e2e2e;
    --white: #ffffff;
    --brand-blue: #1f4fc8;
    --slogan-teal: #16998a;
    --green-bright: #3cc43a;
    --green-deep: #17ad62;
    --lime: #8fdc2a;
    --blue-mid: #0a7be8;
    --blue-navy: #1b2a86;
    --teal: #1aa6b7;
  }
  * { margin: 0; padding: 0; box-sizing: border-box; }
  html, body { width: 933px; height: 1200px; overflow: hidden; }
  body {
    background: var(--canvas);
    font-family: "Poppins", sans-serif;
    position: relative;
  }
  .card {
    position: absolute;
    left: 105px;
    width: 723px;
    height: 412px;
    display: block;
  }
  .card--front { top: 133px; }
  .card--back { top: 655px; }
  .brand-name { font-family: "Poppins", sans-serif; font-weight: 600; fill: var(--brand-blue); letter-spacing: 0.5px; }
  .brand-mark { fill: var(--brand-blue); }
  .slogan { font-family: "Poppins", sans-serif; font-weight: 700; fill: var(--slogan-teal); letter-spacing: 0.9px; }
  .person-name { font-family: "Poppins", sans-serif; font-weight: 700; fill: var(--white); letter-spacing: 0.3px; }
  .person-role { font-family: "Poppins", sans-serif; font-weight: 500; fill: var(--white); letter-spacing: 1.4px; }
  .contact-text { font-family: "Poppins", sans-serif; font-weight: 400; fill: var(--white); }
  .contact-icon { fill: var(--white); }
  .contact-icon-line { fill: none; stroke: var(--white); stroke-width: 1; }
</style>
</head>
<body>

<!-- Front of the card -->
<svg class="card card--front" viewBox="0 0 525 300" aria-label="Business card front">
  <defs>
    <linearGradient id="front-bg" x1="0" y1="0" x2="1" y2="0.6">
      <stop offset="0" stop-color="var(--green-bright)"/>
      <stop offset="0.35" stop-color="var(--blue-mid)"/>
      <stop offset="1" stop-color="var(--blue-navy)"/>
    </linearGradient>
    <linearGradient id="front-arc" x1="0" y1="0" x2="0.6" y2="1">
      <stop offset="0" stop-color="#0f86d8"/>
      <stop offset="0.6" stop-color="var(--green-deep)"/>
      <stop offset="1" stop-color="var(--green-bright)"/>
    </linearGradient>
    <clipPath id="front-clip"><rect width="525" height="300"/></clipPath>
  </defs>
  <g clip-path="url(#front-clip)">
    <rect class="front-background" width="525" height="300" fill="url(#front-bg)"/>
    <path class="swoosh swoosh--outer" d="M210 -10 A270 270 0 0 0 150 320" fill="none" stroke="var(--white)" stroke-width="22" stroke-linecap="round"/>
    <path class="swoosh swoosh--middle" d="M185 -10 A230 230 0 0 0 160 320" fill="none" stroke="none"/>
    <path class="swoosh swoosh--inner-white" d="M268 -20 A215 215 0 0 0 168 240" fill="none" stroke="var(--white)" stroke-width="22" stroke-linecap="round"/>
    <circle class="front-disc" cx="381" cy="153" r="150" fill="var(--white)"/>
    <path class="swoosh swoosh--colour" d="M194 166 A188 188 0 0 0 488 262" fill="none" stroke="var(--white)" stroke-width="36" stroke-linecap="round"/>
    <path class="swoosh swoosh--colour-fill" d="M194 166 A188 188 0 0 0 488 262" fill="none" stroke="url(#front-arc)" stroke-width="18" stroke-linecap="round"/>
    <circle class="accent-dot" cx="513" cy="228" r="15" fill="var(--lime)"/>
    <circle class="brand-mark" cx="286" cy="144" r="18"/>
    <text class="brand-name" x="312" y="154" font-size="25">LARKFIELD</text>
    <text class="slogan" x="331" y="178" font-size="7">REACH YOUR FULL POTENTIAL</text>
  </g>
</svg>

<!-- Back of the card -->
<svg class="card card--back" viewBox="0 0 525 300" aria-label="Business card back">
  <defs>
    <linearGradient id="back-bg" x1="0" y1="0" x2="0.5" y2="1">
      <stop offset="0" stop-color="#0d8ad8"/>
      <stop offset="0.55" stop-color="var(--blue-mid)"/>
      <stop offset="1" stop-color="var(--blue-navy)"/>
    </linearGradient>
    <linearGradient id="back-arc" x1="0" y1="0" x2="1" y2="1">
      <stop offset="0" stop-color="var(--green-deep)"/>
      <stop offset="1" stop-color="var(--green-bright)"/>
    </linearGradient>
    <clipPath id="back-clip"><rect width="525" height="300"/></clipPath>
  </defs>
  <g clip-path="url(#back-clip)">
    <rect class="back-background" width="525" height="300" fill="url(#back-bg)"/>
    <path class="back-panel" d="M300 300 A290 290 0 0 1 310 0 L525 0 L525 300 Z" fill="var(--white)"/>
    <polygon class="top-band" points="312,0 364,0 356,12 304,12" fill="var(--teal)"/>
    <polygon class="top-band" points="384,0 525,0 525,12 376,12" fill="var(--teal)"/>
    <path class="stripe" d="M291 104 A269 269 0 0 0 560 373" fill="none" stroke="url(#back-arc)" stroke-width="24"/>
    <path class="stripe" d="M346 104 A214 214 0 0 0 560 318" fill="none" stroke="url(#back-arc)" stroke-width="24"/>
    <path class="stripe" d="M401 104 A159 159 0 0 0 560 263" fill="none" stroke="url(#back-arc)" stroke-width="24"/>
    <circle class="brand-mark" cx="316" cy="55" r="17"/>
    <text class="brand-name" x="340" y="64" font-size="23">LARKFIELD</text>
    <text class="slogan" x="357" y="83" font-size="6.5">REACH YOUR FULL POTENTIAL</text>

    <text class="person-name" x="16" y="82" font-size="16">MARLON TESWICK</text>
    <text class="person-role" x="16" y="95" font-size="8">DESIGNATION</text>

    <g class="contact-line">
      <path class="contact-icon" d="M17 134 q1 -1 2 0 l1.5 2 q0.5 1 -0.5 1.5 q1 2.5 3 3.5 q0.5 -1 1.5 -0.5 l2 1.5 q1 1 0 2 q-1.5 1.5 -3.5 0.5 q-5 -3 -6.5 -7 q-0.5 -2 0.5 -3.5 Z"/>
      <text class="contact-text" x="34" y="143" font-size="10">094 71 38 206</text>
    </g>
    <g class="contact-line">
      <rect class="contact-icon-line" x="16" y="165" width="10" height="7"/>
      <path class="contact-icon-line" d="M16 165 L21 169 L26 165"/>
      <text class="contact-text" x="34" y="172" font-size="10">larkfieldreach@mail.com</text>
    </g>
    <g class="contact-line">
      <path class="contact-icon" d="M20.5 192 a4 4 0 0 1 4 4 c0 3 -4 7 -4 7 c0 0 -4 -4 -4 -7 a4 4 0 0 1 4 -4 Z M20.5 194.5 a1.5 1.5 0 1 0 0.01 0 Z" fill-rule="evenodd"/>
      <text class="contact-text" x="34" y="201" font-size="10">Alder Bay 204-118 Quarry Rd.</text>
    </g>
    <g class="contact-line">
      <circle class="contact-icon-line" cx="21" cy="226" r="4.5"/>
      <ellipse class="contact-icon-line" cx="21" cy="226" rx="2" ry="4.5"/>
      <path class="contact-icon-line" d="M16.5 226 H25.5"/>
      <text class="contact-text" x="34" y="229" font-size="10">www.larkfieldreach.com</text>
    </g>
  </g>
</svg>

</body>
</html>
```